Summit Builders Web Site / Business Cards

Construction Company that specializes in Water and Fire Damage, Residential ReModels, Landscaping and Building ADU (Accessory Dwelling Unit)

Growing and changing families often need additional space, and a remodeling project can often provide that. Adding a new area, or repurposing an existing one can satisfy this requirement.

Other times, homeowners want to update the look in their kitchen or bathroom with more than just a change of cabinetry or vanity doors and drawers. Whatever your needs are, Summit Builders has skilled workers who are bonded and insured, and ready to make your dreams and visions a reality.

Target Market(s)

Home Owners

Industry/Entity Type

Construction Company

Contact Information for Business Card

Center Logo with our information on the corners

Back side to be Logo Only
Contact Info
CSLB License # 4829516
info@summitbuildersca.example
www.summitbuildersca.example

Coding

Coded - Design and coding required

Number of Pages Required

5+ page

Font styles to use
Serif
Sans Serif

Requirements
Must have
• Using our Logo Colors
Home
About Us
Services
Projects / Portfolio
Contact Us
Nice to have
• Colors matching our Logo
Should not have
• Black because it doesnt match our logo

```html
<!DOCTYPE html>
<html lang="en">
<head>
<meta charset="utf-8">
<title>Summit Builders – Home Page and Mobile Version</title>
<link href="https://fonts.googleapis.com/css2?family=Open+Sans:wght@400;600;700;800&family=Montserrat:wght@400;600;700&display=swap" rel="stylesheet">
<style>
:root{
  --orange:#ff6a00;
  --orange-deep:#f05a00;
  --ink:#262626;
  --dark:#2e2e2e;
  --grey:#6f6f6f;
  --light:#f3f3f3;
  --line:#d9d9d9;
  --white:#ffffff;
}
*{box-sizing:border-box;margin:0;padding:0}
html,body{width:1200px;height:5251px;overflow:hidden}
body{background:#ececec;font-family:"Open Sans",Arial,sans-serif;color:var(--ink);position:relative}
.label{position:absolute;font-family:"Montserrat",Arial,sans-serif;font-weight:400;color:var(--ink)}
.label--home{left:50px;top:48px;font-size:34px}
.label--mobile{left:830px;top:48px;font-size:30px}

/* ---------- shared ---------- */
.page{position:absolute;background:var(--white);box-shadow:0 4px 24px rgba(0,0,0,.18);overflow:hidden}
.sec{position:relative;overflow:hidden}
.abs{position:absolute}
.brand{display:flex;align-items:center;gap:6px;font-weight:800;color:var(--ink);letter-spacing:.5px}
.brand__mark{background:var(--orange);display:block}
.btn{display:inline-block;background:var(--orange);color:var(--white);font-weight:700;text-transform:uppercase;letter-spacing:.5px}
.title{font-weight:700;text-transform:uppercase;text-align:center;letter-spacing:.3px}
.photo{display:block}
.photo--kitchen{background:linear-gradient(110deg,#b49576 0%,#d8cfc4 35%,#eeeeec 60%,#c9c6c1 100%)}
.photo--interior{background:linear-gradient(90deg,#3c3c3c 0%,#6c6c6c 30%,#ececec 55%,#d8d8d8 100%)}
.photo--city{background:linear-gradient(160deg,#8fb3d3,#3c5f80)}
.photo--white{background:linear-gradient(160deg,#f6f6f6,#c7c9cc)}
.photo--blue{background:linear-gradient(160deg,#e7e7e7 0%,#e7e7e7 55%,#2d4f8a 56%,#2d4f8a 100%)}
.photo--home{background:linear-gradient(160deg,#a9c2d8,#6e7f62)}
.photo--modern{background:linear-gradient(160deg,#fafafa,#9a9a9a)}
.photo--tower{background:linear-gradient(160deg,#a8c7e3,#557a9c)}
.photo--orange{background:radial-gradient(circle at 30% 40%,#ff8a2a,var(--orange-deep) 70%)}
.avatar{border-radius:50%;background:linear-gradient(160deg,#d8d8d8,#9a9a9a);border:3px solid var(--white);box-shadow:0 0 0 1px var(--line)}
.arrows{display:flex;gap:5px;justify-content:center}
.arrows span{width:22px;height:22px;border:1px solid #9a9a9a;border-radius:50%;display:flex;align-items:center;justify-content:center;font-size:12px;color:#777}

/* ---------- desktop home page ---------- */
.desk{left:50px;top:110px;width:680px;height:3200px;font-size:6px}
.d-nav{height:40px;display:flex;align-items:center;padding:0 36px}
.d-nav .brand{font-size:9px}
.d-nav .brand__mark{width:12px;height:12px}
.d-nav__links{display:flex;gap:14px;margin-left:auto;font-size:6.5px;color:#444}
.d-nav__phone{margin-left:22px;font-size:6.5px;font-weight:700}
.d-hero{height:300px}
.d-hero .photo{position:absolute;inset:0}
.d-hero__panel{position:absolute;left:36px;top:28px;width:170px;height:150px;background:rgba(255,255,255,.92);padding:16px 10px}
.d-hero__best{font-size:15px;line-height:1.1}
.d-hero__why{font-size:12px}
.d-hero__deliver{font-size:20px;font-weight:800;line-height:1.15}
.d-hero__text{font-size:6px;color:#444;margin:4px 0 7px;line-height:1.4}
.d-hero .btn{font-size:5.5px;padding:5px 10px}
.d-spec{height:330px;padding-top:18px}
.d-spec .title{font-size:10px}
.d-spec__cards{display:flex;justify-content:center;gap:36px;margin-top:20px}
.d-card{position:relative;width:130px;height:170px;text-align:center;padding:42px 12px 0;filter:drop-shadow(0 2px 4px rgba(0,0,0,.15))}
.d-card::before{content:"";position:absolute;inset:0;background:var(--white);clip-path:polygon(50% 0,100% 18%,100% 100%,0 100%,0 18%);z-index:-1}
.d-card__icon{display:block;margin:0 auto 6px}
.d-card__name{color:var(--orange);font-weight:700;font-size:6px;text-transform:uppercase;line-height:1.3}
.d-card__text{color:var(--grey);font-size:5.5px;margin-top:4px;line-height:1.4}
.d-card__foot{position:absolute;left:50%;bottom:0;transform:translateX(-50%);width:0;height:0;border-left:16px solid transparent;border-right:16px solid transparent;border-bottom:16px solid var(--dark)}
.d-about{height:320px;background:var(--light)}
.d-about__text{position:absolute;left:365px;top:100px;width:240px}
.d-about__text h3{font-size:10px;font-weight:700;margin-bottom:6px}
.d-about__text p{font-size:5.5px;color:#555;line-height:1.5;margin-bottom:8px}
.d-about .btn{font-size:5px;padding:5px 14px}
.d-services{height:380px;color:var(--white)}
.d-services .title{position:relative;font-size:10px;padding-top:60px}
.d-svc-grid{position:relative;display:grid;grid-template-columns:repeat(3,130px);gap:18px 46px;margin:24px 0 0 40px}
.d-svc__icon{display:block;margin-bottom:4px}
.d-svc__name{font-size:5.5px;font-weight:700;text-transform:uppercase}
.d-svc__text{font-size:5px;opacity:.9;line-height:1.4;margin-top:2px}
.d-testi{height:340px;padding-top:24px}
.d-testi .title{font-size:10px}
.d-testi__cards{display:flex;justify-content:center;gap:40px;margin-top:16px}
.d-quote{width:200px;height:140px;background:var(--white);box-shadow:0 1px 6px rgba(0,0,0,.15);text-align:center;padding:36px 16px 0;position:relative;margin-top:22px}
.d-quote .avatar{position:absolute;left:50%;top:-22px;transform:translateX(-50%);width:42px;height:42px}
.d-quote p{font-size:5.5px;color:#444;line-height:1.45}
.d-quote b{display:block;font-size:5px;margin-top:8px}
.d-quote small{font-size:5px;color:#666}
.d-why{height:360px;color:var(--white)}
.d-why .title{position:relative;font-size:10px;padding-top:80px}
.d-why__list{position:relative;display:flex;justify-content:center;gap:52px;margin-top:30px;text-align:center}
.d-why__item{width:80px;font-size:6px;font-weight:700;line-height:1.3}
.d-why__item svg{display:block;margin:0 auto 6px}
.d-proj{height:420px;padding-top:26px;text-align:center}
.d-proj .title{font-size:10px}
.d-proj__grid{display:grid;grid-template-columns:repeat(3,115px);grid-auto-rows:85px;gap:6px;justify-content:center;margin:16px 0 14px}
.d-proj .btn{font-size:5px;padding:5px 14px}
.d-comp{height:220px;color:var(--white)}
.d-comp .title{position:relative;font-size:10px;padding-top:40px}
.d-stats{position:relative;display:flex;justify-content:center;gap:22px;margin-top:30px}
.d-stat{width:68px;height:68px;border-radius:50%;overflow:hidden;background:var(--white);box-shadow:0 0 0 3px var(--white),0 0 0 4px var(--line);text-align:center}
.d-stat b{display:block;background:var(--dark);height:32px;line-height:40px;font-size:12px}
.d-stat span{display:block;color:var(--ink);font-size:5px;font-weight:700;padding-top:6px;text-transform:uppercase;line-height:1.3}
.d-news{height:170px;text-align:center;padding-top:18px}
.d-news .title{font-size:9px}
.d-news__input{width:160px;height:16px;border:1px solid var(--line);margin:12px auto 6px;font-size:4.5px;color:#999;line-height:14px}
.d-news .btn{font-size:4.5px;padding:4px 10px}
.d-foot{height:300px;background:var(--dark);color:#ddd}
.d-foot__cols{position:absolute;left:36px;top:150px;right:36px;display:flex}
.d-foot .brand{color:var(--white);font-size:9px;margin-top:14px}
.d-foot .brand__mark{width:12px;height:12px}
.d-foot__col{font-size:5px;line-height:1.9}
.d-foot__col h4{font-size:6px;font-weight:600;margin-bottom:4px;color:var(--white)}

/* ---------- mobile ---------- */
.mob{left:830px;top:110px;width:260px;height:4890px;font-size:10px}
.m-nav{height:55px;display:flex;align-items:center;padding:0 12px;justify-content:space-between}
.m-nav .brand{font-size:10px}
.m-nav .brand__mark{width:14px;height:14px}
.m-burger{width:20px;height:14px;display:flex;flex-direction:column;justify-content:space-between}
.m-burger i{display:block;height:2px;background:var(--ink)}
.m-hero{height:355px}
.m-hero .photo{position:absolute;left:0;top:0;width:100%;height:120px}
.m-hero__body{position:absolute;top:120px;left:0;right:0;text-align:center;padding-top:28px}
.m-hero__best{font-size:16px;line-height:1.1}
.m-hero__why{font-size:13px}
.m-hero__deliver{font-size:21px;font-weight:800;line-height:1.15}
.m-hero__text{font-size:10.5px;color:#333;margin:5px 20px 14px;line-height:1.4}
.m-hero .btn{font-size:10px;padding:8px 16px}
.m-spec{height:280px;text-align:center;padding-top:30px}
.m-card{position:relative;width:230px;height:190px;margin:0 auto;padding-top:40px;filter:drop-shadow(0 2px 4px rgba(0,0,0,.15))}
.m-card::before{content:"";position:absolute;inset:0;background:var(--white);clip-path:polygon(50% 0,100% 18%,100% 100%,0 100%,0 18%);z-index:-1}
.m-card__name{color:var(--orange);font-weight:700;font-size:12px;margin-top:6px;line-height:1.25}
.m-card__text{color:#444;font-size:11px;margin:6px 16px 0;line-height:1.35}
.m-spec .arrows{margin-top:14px}
.m-aboutimg{height:325px;background:var(--light)}
.m-about{height:335px;background:var(--light);padding:10px 12px 0}
.m-about h3{font-size:16px;font-weight:700;margin-bottom:6px}
.m-about p{font-size:10.5px;color:#444;line-height:1.55;margin-bottom:10px}
.m-about .btn{font-size:10px;padding:7px 14px}
.m-services{height:510px;color:var(--white)}
.m-services .title{position:relative;font-size:15px;padding-top:40px}
.m-svc-grid{position:relative;display:grid;grid-template-columns:1fr 1fr;gap:24px 10px;padding:16px 10px 0}
.m-svc{font-size:10.5px;line-height:1.25;text-transform:uppercase}
.m-svc svg{display:block;margin-bottom:6px}
.m-testi{height:510px;text-align:center;padding-top:54px}
.m-testi .title{font-size:15px}
.m-testi .avatar{width:64px;height:64px;margin:14px auto 10px;display:block}
.m-testi p{font-size:11px;color:#333;line-height:1.55;margin:0 24px}
.m-testi b{display:block;font-size:11px;margin-top:12px}
.m-testi small{font-size:11px;color:#444;display:block;margin-bottom:10px}
.m-why{height:380px;color:var(--white);text-align:center}
.m-why .title{position:relative;font-size:15px;padding-top:56px}
.m-why svg.icon{position:relative;display:block;margin:22px auto 8px}
.m-why__name{position:relative;font-size:13px;font-weight:700;line-height:1.3}
.m-why .arrows{position:relative;margin-top:6px}
.m-why .arrows span{border-color:rgba(255,255,255,.6);color:var(--white)}
.m-proj{height:380px;text-align:center;padding-top:40px;background:var(--light)}
.m-proj .title{font-size:16px}
.m-proj .photo{width:200px;height:180px;margin:12px auto 12px}
.m-proj .btn{font-size:10.5px;padding:8px 22px}
.m-proj .arrows{margin-top:14px}
.m-comp{height:390px;color:var(--white);text-align:center}
.m-comp .title{position:relative;font-size:15px;padding-top:62px}
.m-stat{position:relative;width:190px;height:190px;border-radius:50%;overflow:hidden;background:var(--white);margin:36px auto 8px;box-shadow:0 0 0 4px var(--white),0 0 0 5px var(--line)}
.m-stat b{display:block;background:var(--ink);height:92px;line-height:120px;font-size:32px}
.m-stat span{display:block;color:var(--ink);font-weight:700;font-size:13px;padding-top:14px;line-height:1.3}
.m-news{height:315px;text-align:center;padding-top:30px}
.m-news .title{font-size:16px;line-height:1.3}
.m-news__input{height:44px;border-top:1px solid var(--line);border-bottom:1px solid var(--line);margin:14px 0 18px;font-size:10px;color:#666;line-height:42px;letter-spacing:1px}
.m-news .btn{font-size:10.5px;padding:10px 24px}
.m-foot{height:1050px;background:var(--dark);color:#ddd;font-size:10.5px;padding:0 10px}
.m-foot .brand{color:var(--white);font-size:14px;margin-top:120px}
.m-foot .brand__mark{width:18px;height:18px}
.m-foot h4{font-size:13px;font-weight:400;color:var(--white);margin:48px 0 10px}
.m-foot ul{list-style:none;line-height:2.6}
.m-contact{display:flex;gap:10px;margin-top:18px;line-height:1.6}
.m-contact svg{flex:none;margin-top:3px}
.m-hours p{margin-bottom:12px;line-height:1.4}
.m-copy{font-size:8.5px;margin-top:20px;line-height:1.8}
</style>
</head>
<body>

<div class="label label--home">Home Page</div>
<div class="label label--mobile">Mobile Version</div>

<!-- ================= Desktop home page ================= -->
<main class="page desk">
  <header class="d-nav">
    <div class="brand"><span class="brand__mark"></span>SUMMIT BUILDERS</div>
    <nav class="d-nav__links"><span>Home</span><span>About Us</span><span>Services</span><span>Projects / Portfolio</span><span>Contact Us</span></nav>
    <div class="d-nav__phone">&#9742; 1 555 310 4420</div>
  </header>

  <section class="sec d-hero">
    <div class="photo photo--kitchen" role="img" aria-label="Bright modern kitchen with wood cabinets"></div>
    <div class="d-hero__panel">
      <div class="d-hero__best">THE BEST</div>
      <div class="d-hero__why">Choose Us Because</div>
      <div class="d-hero__deliver">WE DELIVER</div>
      <p class="d-hero__text">We are rethoric question ran over her cheek When she reached the first hills of the Italic Mountains.</p>
      <span class="btn">Get a quote</span>
    </div>
    <svg class="abs" style="left:0;bottom:0" width="680" height="110" viewBox="0 0 680 110">
      <polygon points="0,30 330,110 0,110" fill="#3a3a3a"/>
      <polygon points="0,50 340,110 680,20 680,110 0,110" fill="#fff"/>
      <polyline points="200,70 340,108 680,14" fill="none" stroke="#ff6a00" stroke-width="3"/>
    </svg>
  </section>

  <section class="sec d-spec">
    <h2 class="title">We specializes in</h2>
    <div class="d-spec__cards">
      <article class="d-card">
        <svg class="d-card__icon" width="26" height="22" viewBox="0 0 26 22"><rect x="3" y="8" width="20" height="13" fill="none" stroke="#ff6a00" stroke-width="1.5"/><polyline points="1,9 13,1 25,9" fill="none" stroke="#ff6a00" stroke-width="1.5"/><rect x="10" y="13" width="6" height="8" fill="#ff6a00"/></svg>
        <div class="d-card__name">Water<br>and fire damage</div>
        <p class="d-card__text">It is a long established fact that a reader will be</p>
        <span class="d-card__foot"></span>
      </article>
      <article class="d-card">
        <svg class="d-card__icon" width="26" height="22" viewBox="0 0 26 22"><rect x="2" y="6" width="22" height="15" fill="none" stroke="#ff6a00" stroke-width="1.5"/><line x1="2" y1="12" x2="24" y2="12" stroke="#ff6a00" stroke-width="1.5"/><line x1="13" y1="6" x2="13" y2="21" stroke="#ff6a00" stroke-width="1.5"/></svg>
        <div class="d-card__name">Residential<br>remodels</div>
        <p class="d-card__text">It is a long established fact that a reader will be</p>
        <span class="d-card__foot"></span>
      </article>
      <article class="d-card">
        <svg class="d-card__icon" width="26" height="22" viewBox="0 0 26 22"><polyline points="2,10 13,2 24,10" fill="none" stroke="#ff6a00" stroke-width="1.5"/><rect x="5" y="10" width="16" height="11" fill="none" stroke="#ff6a00" stroke-width="1.5"/><rect x="9" y="13" width="8" height="5" fill="#ff6a00"/></svg>
        <div class="d-card__name">Landscaping and<br>building ADU</div>
        <p class="d-card__text">It is a long established fact that a reader will be</p>
        <span class="d-card__foot"></span>
      </article>
    </div>
  </section>

  <section class="sec d-about">
    <svg class="abs" style="right:0;top:0" width="380" height="30" viewBox="0 0 380 30">
      <polygon points="0,30 380,0 380,30" fill="#cfcfcf"/>
      <g stroke="#9a9a9a" stroke-width="1">
        <line x1="200" y1="30" x2="200" y2="14"/><line x1="210" y1="30" x2="210" y2="13"/><line x1="220" y1="30" x2="220" y2="12"/><line x1="230" y1="30" x2="230" y2="12"/><line x1="240" y1="30" x2="240" y2="11"/><line x1="250" y1="30" x2="250" y2="10"/><line x1="260" y1="30" x2="260" y2="9"/><line x1="270" y1="30" x2="270" y2="8"/><line x1="280" y1="30" x2="280" y2="7"/><line x1="290" y1="30" x2="290" y2="7"/><line x1="300" y1="30" x2="300" y2="6"/><line x1="310" y1="30" x2="310" y2="5"/><line x1="320" y1="30" x2="320" y2="4"/><line x1="330" y1="30" x2="330" y2="3"/><line x1="340" y1="30" x2="340" y2="2"/><line x1="350" y1="30" x2="350" y2="2"/><line x1="360" y1="30" x2="360" y2="1"/><line x1="370" y1="30" x2="370" y2="0"/>
      </g>
    </svg>
    <div class="abs photo photo--interior" style="left:34px;top:40px;width:300px;height:130px;top:50px;height:170px;clip-path:polygon(0 20%,30% 0,100% 30%,100% 100%,0 100%)" role="img" aria-label="Modern interior with dark cabinetry and orange slatted wall"></div>
    <div class="d-about__text">
      <h3>ABOUT US</h3>
      <p>We are rethoric question ran over her cheek When she reached the first hills of the Italic Mountains, she had a last view back on the skyline of her hometown Bookmarksgrove, the headline of Alphabet Village and the subline of her own road, the Line Lane.</p>
      <span class="btn">Read more</span>
    </div>
  </section>

  <section class="sec d-services">
    <div class="abs photo photo--orange" style="inset:0;clip-path:polygon(0 8%,50% 0,100% 8%,100% 92%,0 100%)" role="img" aria-label="Orange toned construction background"></div>
    <h2 class="title">Services</h2>
    <div class="d-svc-grid">
      <div class="d-svc"><svg class="d-svc__icon" width="12" height="11" viewBox="0 0 12 11"><polygon points="6,0 12,5 10,5 10,11 2,11 2,5 0,5" fill="#fff"/></svg><div class="d-svc__name">Home construction</div><p class="d-svc__text">It is a long established fact that a reader will be distracted.</p></div>
      <div class="d-svc"><svg class="d-svc__icon" width="12" height="11" viewBox="0 0 12 11"><rect x="1" y="3" width="10" height="8" fill="#fff"/><polygon points="0,4 6,0 12,4" fill="#fff"/></svg><div class="d-svc__name">Exterior design</div><p class="d-svc__text">It is a long established fact that a reader will be distracted.</p></div>
      <div class="d-svc"><svg class="d-svc__icon" width="12" height="11" viewBox="0 0 12 11"><rect x="2" y="1" width="8" height="10" fill="#fff"/></svg><div class="d-svc__name">Building remodeling</div><p class="d-svc__text">It is a long established fact that a reader will be distracted.</p></div>
      <div class="d-svc"><svg class="d-svc__icon" width="12" height="11" viewBox="0 0 12 11"><polyline points="1,10 6,2 11,10" fill="none" stroke="#fff" stroke-width="2"/></svg><div class="d-svc__name">Renovations</div><p class="d-svc__text">It is a long established fact that a reader will be distracted.</p></div>
      <div class="d-svc"><svg class="d-svc__icon" width="12" height="11" viewBox="0 0 12 11"><rect x="0" y="6" width="12" height="5" fill="#fff"/><circle cx="6" cy="3" r="2.5" fill="#fff"/></svg><div class="d-svc__name">Interior design</div><p class="d-svc__text">It is a long established fact that a reader will be distracted.</p></div>
      <div class="d-svc"><svg class="d-svc__icon" width="12" height="11" viewBox="0 0 12 11"><rect x="2" y="3" width="8" height="8" fill="#fff"/><rect x="4" y="0" width="4" height="4" fill="none" stroke="#fff"/></svg><div class="d-svc__name">Safety management</div><p class="d-svc__text">It is a long established fact that a reader will be distracted.</p></div>
    </div>
  </section>

  <section class="sec d-testi">
    <h2 class="title">Testimonial</h2>
    <div class="d-testi__cards">
      <div class="d-quote">
        <span class="avatar" role="img" aria-label="Portrait of client"></span>
        <p>"...and for all the wonderful work you and your crew are doing. Our team has nothing but good things to say - we are really fortunate to have found you for this project!"</p>
        <b>SAM CARTER</b><small>Chairman Northfield Group</small>
      </div>
      <div class="d-quote">
        <span class="avatar" role="img" aria-label="Portrait of client"></span>
        <p>Summit Builders is one of the best general contractors we've worked with. The entire team tactfully delivered a project of exceptional quality while staying on schedule and under budget.</p>
        <b>LENA ORTIZ</b><small>Chairman Northfield Group</small>
      </div>
    </div>
  </section>

  <section class="sec d-why">
    <svg class="abs" style="left:0;top:0" width="680" height="360" viewBox="0 0 680 360">
      <g stroke="#9a9a9a" stroke-width="1"><line x1="10" y1="0" x2="10" y2="30"/><line x1="20" y1="0" x2="20" y2="28"/><line x1="30" y1="0" x2="30" y2="27"/><line x1="40" y1="0" x2="40" y2="26"/><line x1="50" y1="0" x2="50" y2="25"/><line x1="60" y1="0" x2="60" y2="24"/><line x1="70" y1="0" x2="70" y2="23"/><line x1="80" y1="0" x2="80" y2="22"/><line x1="90" y1="0" x2="90" y2="21"/><line x1="100" y1="0" x2="100" y2="20"/></g>
      <polygon points="0,50 680,0 680,250 340,300 0,230" fill="#ff6a00"/>
      <polygon points="420,300 680,220 680,260" fill="#3a3a3a"/>
    </svg>
    <h2 class="title">Why choose us</h2>
    <div class="d-why__list">
      <div class="d-why__item"><svg width="26" height="26" viewBox="0 0 26 26"><circle cx="13" cy="10" r="8" fill="none" stroke="#fff" stroke-width="1.5"/><polyline points="8,17 6,25 13,21 20,25 18,17" fill="none" stroke="#fff" stroke-width="1.5"/></svg>We've Reputation For Excellence</div>
      <div class="d-why__item"><svg width="26" height="26" viewBox="0 0 26 26"><polyline points="2,14 9,8 17,14 24,8" fill="none" stroke="#fff" stroke-width="1.5"/><rect x="6" y="14" width="14" height="8" fill="none" stroke="#fff" stroke-width="1.5"/></svg>We Build Partnerships</div>
      <div class="d-why__item"><svg width="26" height="26" viewBox="0 0 26 26"><circle cx="13" cy="13" r="4" fill="none" stroke="#fff" stroke-width="1.5"/><g stroke="#fff" stroke-width="1.5"><line x1="13" y1="2" x2="13" y2="7"/><line x1="13" y1="19" x2="13" y2="24"/><line x1="2" y1="13" x2="7" y2="13"/><line x1="19" y1="13" x2="24" y2="13"/></g></svg>Guided By Commitment</div>
      <div class="d-why__item"><svg width="26" height="26" viewBox="0 0 26 26"><circle cx="8" cy="9" r="3" fill="none" stroke="#fff" stroke-width="1.5"/><circle cx="18" cy="9" r="3" fill="none" stroke="#fff" stroke-width="1.5"/><path d="M2 22c0-5 12-5 12 0M12 22c0-5 12-5 12 0" fill="none" stroke="#fff" stroke-width="1.5"/></svg>A Team Of Professionals</div>
    </div>
  </section>

  <section class="sec d-proj">
    <h2 class="title">Projects</h2>
    <div class="d-proj__grid">
      <div class="photo photo--tower" role="img" aria-label="Glass office tower"></div>
      <div class="photo photo--white" role="img" aria-label="White kitchen interior"></div>
      <div class="photo photo--modern" role="img" aria-label="Modern white house exterior"></div>
      <div class="photo photo--city" role="img" aria-label="Commercial building at dusk"></div>
      <div class="photo photo--blue" role="img" aria-label="Kitchen with blue cabinets"></div>
      <div class="photo photo--home" role="img" aria-label="Suburban family home"></div>
    </div>
    <span class="btn">View more</span>
  </section>

  <section class="sec d-comp">
    <svg class="abs" style="left:0;top:0" width="680" height="220" viewBox="0 0 680 220">
      <polygon points="0,0 680,0 680,60 0,60" fill="#fff"/>
      <polygon points="0,20 680,0 680,140 0,140" fill="#ff6a00"/>
    </svg>
    <h2 class="title">Company</h2>
    <div class="d-stats">
      <div class="d-stat"><b>53</b><span>Total<br>projects</span></div>
      <div class="d-stat"><b>371</b><span>Staff<br>members</span></div>
      <div class="d-stat"><b>15</b><span>Working in<br>states</span></div>
      <div class="d-stat"><b>2600</b><span>Hours<br>for work</span></div>
    </div>
  </section>

  <section class="sec d-news">
    <h2 class="title">Newsletter subscribe</h2>
    <div class="d-news__input">ENTER YOUR MAIL ID</div>
    <span class="btn">Subscribe now</span>
  </section>

  <footer class="sec d-foot">
    <svg class="abs" style="left:0;top:0" width="680" height="90" viewBox="0 0 680 90">
      <polygon points="0,0 680,0 680,20 340,80 0,20" fill="#fff"/>
      <polyline points="80,40 340,86 600,40" fill="none" stroke="#ff6a00" stroke-width="3"/>
    </svg>
    <div class="d-foot__cols">
      <div style="width:200px"><div class="brand"><span class="brand__mark"></span>SUMMIT BUILDERS</div></div>
      <div class="d-foot__col" style="width:160px"><h4>Quick Link</h4>Home<br>About Us<br>Services<br>Projects / Portfolio<br>Contact Us</div>
      <div class="d-foot__col" style="width:150px"><h4>Contact Us</h4>214 Ridgeview Ave<br>Fairmont, CA 90000<br>555-310-4420<br>555-208-7731<br>555-310-4490</div>
      <div class="d-foot__col"><h4>Hours</h4>Monday – friday:<br>10:00 – 16:00<br>Saturday:<br>12:00 – 15:00<br>sunday and holidays:<br>09:00 – 12:00</div>
    </div>
  </footer>
</main>

<!-- ================= Mobile version ================= -->
<main class="page mob">
  <header class="m-nav">
    <div class="brand"><span class="brand__mark"></span>SUMMIT BUILDERS</div>
    <div class="m-burger"><i></i><i></i><i></i></div>
  </header>

  <section class="sec m-hero">
    <div class="photo photo--kitchen" role="img" aria-label="Bright modern kitchen with wood cabinets"></div>
    <svg class="abs" style="left:0;top:90px" width="260" height="50" viewBox="0 0 260 50">
      <polygon points="0,10 130,50 260,10 260,50 0,50" fill="#fff"/>
      <polyline points="60,30 130,48 260,8" fill="none" stroke="#ff6a00" stroke-width="3"/>
    </svg>
    <div class="m-hero__body">
      <div class="m-hero__best">THE BEST</div>
      <div class="m-hero__why">Choose Us because</div>
      <div class="m-hero__deliver">WE DELIVER</div>
      <p class="m-hero__text">We are rethoric question ran over her cheek When she reached the first hills of the Italic Mountains.</p>
      <span class="btn">Get a quote</span>
    </div>
  </section>

  <section class="sec m-spec">
    <div class="m-card">
      <svg width="32" height="28" viewBox="0 0 26 22"><rect x="3" y="8" width="20" height="13" fill="none" stroke="#ff6a00" stroke-width="1.5"/><polyline points="1,9 13,1 25,9" fill="none" stroke="#ff6a00" stroke-width="1.5"/><rect x="10" y="13" width="6" height="8" fill="#ff6a00"/></svg>
      <div class="m-card__name">WATER<br>AND FIRE DAMAGE</div>
      <p class="m-card__text">It is a long established fact that a reader will be</p>
    </div>
    <div class="arrows"><span>&#8249;</span><span>&#8250;</span></div>
  </section>

  <section class="sec m-aboutimg">
    <svg class="abs" style="right:0;top:0" width="180" height="20" viewBox="0 0 180 20"><g stroke="#9a9a9a"><line x1="10" y1="20" x2="10" y2="10"/><line x1="20" y1="20" x2="20" y2="9"/><line x1="30" y1="20" x2="30" y2="8"/><line x1="40" y1="20" x2="40" y2="8"/><line x1="50" y1="20" x2="50" y2="7"/><line x1="60" y1="20" x2="60" y2="6"/><line x1="70" y1="20" x2="70" y2="6"/><line x1="80" y1="20" x2="80" y2="5"/><line x1="90" y1="20" x2="90" y2="4"/><line x1="100" y1="20" x2="100" y2="4"/><line x1="110" y1="20" x2="110" y2="3"/><line x1="120" y1="20" x2="120" y2="2"/><line x1="130" y1="20" x2="130" y2="2"/><line x1="140" y1="20" x2="140" y2="1"/><line x1="150" y1="20" x2="150" y2="1"/><line x1="160" y1="20" x2="160" y2="0"/><line x1="170" y1="20" x2="170" y2="0"/></g></svg>
    <div class="abs photo photo--interior" style="left:10px;top:50px;width:240px;height:260px;clip-path:polygon(0 18%,30% 0,100% 30%,100% 100%,0 100%)" role="img" aria-label="Modern interior with dark cabinetry and orange slatted wall"></div>
  </section>

  <section class="sec m-about">
    <h3>ABOUT US</h3>
    <p>We are rethoric question ran over her cheek When she reached the first hills of the Italic Mountains, she had a last view back on the skyline of her hometown Bookmarksgrove, the headline of Alphabet Village and the subline of her own road, the Line Lane.</p>
    <span class="btn">Read more</span>
  </section>

  <section class="sec m-services">
    <div class="abs photo photo--orange" style="inset:0;clip-path:polygon(0 5%,50% 0,100% 5%,100% 100%,0 100%)" role="img" aria-label="Orange toned construction background"></div>
    <h2 class="title">Services</h2>
    <div class="m-svc-grid">
      <div class="m-svc"><svg width="24" height="22" viewBox="0 0 12 11"><polygon points="6,0 12,5 10,5 10,11 2,11 2,5 0,5" fill="#fff"/></svg>Home construction</div>
      <div class="m-svc"><svg width="24" height="22" viewBox="0 0 12 11"><rect x="1" y="3" width="10" height="8" fill="#fff"/><polygon points="0,4 6,0 12,4" fill="#fff"/></svg>Exterior design</div>
      <div class="m-svc"><svg width="24" height="22" viewBox="0 0 12 11"><rect x="2" y="1" width="8" height="10" fill="#fff"/></svg>Building remodeling</div>
      <div class="m-svc"><svg width="24" height="22" viewBox="0 0 12 11"><rect x="0" y="6" width="12" height="5" fill="#fff"/><circle cx="6" cy="3" r="2.5" fill="#fff"/></svg>Interior design</div>
      <div class="m-svc"><svg width="24" height="22" viewBox="0 0 12 11"><polyline points="1,10 6,2 11,10" fill="none" stroke="#fff" stroke-width="2"/></svg>Renovations</div>
      <div class="m-svc"><svg width="24" height="22" viewBox="0 0 12 11"><rect x="2" y="3" width="8" height="8" fill="#fff"/><rect x="4" y="0" width="4" height="4" fill="none" stroke="#fff"/></svg>Safety management</div>
    </div>
  </section>

  <section class="sec m-testi">
    <h2 class="title">Testimonial</h2>
    <span class="avatar" role="img" aria-label="Portrait of client"></span>
    <p>"...and for all the wonderful work you and your crew are doing. Our team has nothing but good things to say - we are really fortunate to have found you for this project!"</p>
    <b>SAM CARTER</b><small>Chairman Northfield Group</small>
    <div class="arrows"><span>&#8249;</span><span>&#8250;</span></div>
  </section>

  <section class="sec m-why">
    <svg class="abs" style="left:0;top:0" width="260" height="380" viewBox="0 0 260 380"><polygon points="0,20 260,0 260,330 180,380 0,330" fill="#ff6a00"/></svg>
    <h2 class="title">Why choose us</h2>
    <svg class="icon" width="60" height="60" viewBox="0 0 26 26"><circle cx="13" cy="10" r="8" fill="none" stroke="#fff" stroke-width="1.2"/><polyline points="8,17 6,25 13,21 20,25 18,17" fill="none" stroke="#fff" stroke-width="1.2"/></svg>
    <div class="m-why__name">We've Repution<br>For Excellence</div>
    <div class="arrows"><span>&#8249;</span><span>&#8250;</span></div>
  </section>

  <section class="sec m-proj">
    <h2 class="title">Projects</h2>
    <div class="photo photo--blue" role="img" aria-label="Kitchen with white upper and blue lower cabinets"></div>
    <span class="btn">View more</span>
    <div class="arrows"><span>&#8249;</span><span>&#8250;</span></div>
  </section>

  <section class="sec m-comp">
    <svg class="abs" style="left:0;top:0" width="260" height="390" viewBox="0 0 260 390"><rect width="260" height="390" fill="#fff"/><polygon points="0,20 260,0 260,240 0,240" fill="#ff6a00"/></svg>
    <h2 class="title">Company</h2>
    <div class="m-stat"><b>371</b><span>STAFF<br>MEMBERS</span></div>
    <div class="arrows" style="position:relative"><span>&#8249;</span><span>&#8250;</span></div>
  </section>

  <section class="sec m-news">
    <h2 class="title">Newsletter<br>subscribe</h2>
    <div class="m-news__input">ENTER YOUR MAIL ID</div>
    <span class="btn">Subscribe now</span>
  </section>

  <footer class="sec m-foot">
    <svg class="abs" style="left:0;top:0" width="260" height="80" viewBox="0 0 260 80">
      <polygon points="0,0 260,0 260,10 130,60 0,10" fill="#fff"/>
      <polyline points="20,30 130,66 240,30" fill="none" stroke="#fff" stroke-width="3"/>
    </svg>
    <div class="brand"><span class="brand__mark"></span>SUMMIT BUILDERS</div>
    <h4>Quick Link</h4>
    <ul><li>Home</li><li>About Us</li><li>Services</li><li>Projects / Portfolio</li><li>Contact Us</li></ul>
    <div class="m-contact"><svg width="10" height="12" viewBox="0 0 10 12"><path d="M5 0a4 4 0 0 1 4 4c0 3-4 8-4 8S1 7 1 4a4 4 0 0 1 4-4z" fill="#fff"/></svg><span>214 Ridgeview Ave<br>Fairmont, CA 90000</span></div>
    <div class="m-contact"><svg width="10" height="12" viewBox="0 0 10 12"><rect x="2" y="0" width="6" height="12" rx="1" fill="#fff"/></svg><span>555-310-4420<br>555-208-7731</span></div>
    <div class="m-contact"><svg width="10" height="12" viewBox="0 0 10 12"><rect x="0" y="3" width="10" height="8" fill="#fff"/></svg><span>555-310-4490</span></div>
    <h4>Hours</h4>
    <div class="m-hours">
      <p>Monday – friday:<br>10:00 – 16:00</p>
      <p>Saturday:<br>12:00 – 15:00</p>
      <p>sunday and holidays:<br>09:00 – 12:00</p>
    </div>
    <p class="m-copy">Copyright © 2020 · All Rights Reserved ·<br>Summit Builders</p>
  </footer>
</main>

</body>
</html>
```